Hollis Ironworks Business Card

We need a business card design for a new small metal fabrication business in rural NSW, Australia.

The business (Hollis Ironworks) is owner operated by a man with the initials RB - much of the branding comes from this name.

Hollis Ironworks designs, engineers, repairs and manufactures a range of custom, quality metal works including vehicle trays, agricultural machinery impliments, trailers, wood splitters, fire pits, furniture etc.

The brand position focuses on custom work of the highest quality.

Business card design should show quality, attention to detail and stand out among a mass of business cards.

Logos are in the files

The grey color may be changed on the logo if required to stand out more.

There is an image attached of a simple card that is liked because it is clean, clear, simple, masculine and effective. It says 'quality'. As most of the work we do is custom it would be good to have the business card speak to this.

Target Market(s)

Rural and regional based Australians. Primarily adult male 25-60 yrs. Primary production / rural / travelling lifestyle.

Industry/Entity Type

Metal Fabrication

Contact Information for Business Card

The words 'custom quality fabrications' would be great somewhere perhaps on the backside (not on the information side)
Name
title
Phone: 0491 538 274 and (02) 7342 9185
email: info@hollisiw.com.au
www.hollisiw.com.au

address (2 lines)

Requirements
Nice to have
• Background colour should be very navy blue or black.
Should not have
• NO orange and blue combinations.
• Navy is OK

```html
<!DOCTYPE html>
<html lang="en">
<head>
<meta charset="utf-8">
<title>Hollis Ironworks — Business Card</title>
<link rel="stylesheet" href="https://fonts.googleapis.com/css2?family=Montserrat:wght@400;500;600;700&family=Oswald:wght@300;400&display=swap">
<style>
  :root {
    --navy: #232a6e;
    --navy-text: #2a2f72;
    --green: #5cb93a;
    --silver: #c4c6ca;
    --rule: #a9abaf;
    --paper: #ffffff;
    --backdrop: #e6e7ea;
    --muted: #4a4d63;
  }
  * { margin: 0; padding: 0; box-sizing: border-box; }
  html, body {
    width: 1200px; height: 900px; overflow: hidden;
    background: var(--backdrop);
    font-family: "Montserrat", sans-serif;
  }
  .canvas { position: relative; width: 1200px; height: 900px; }

  .card {
    position: absolute;
    width: 680px; height: 388px;
    box-shadow: 0 10px 28px rgba(0,0,0,.18);
  }

  /* Back of card */
  .card-back { left: 140px; top: 40px; background: var(--navy); }
  .card-back .tab {
    position: absolute; width: 16px; height: 10px; background: var(--paper);
  }
  .card-back .tab-top { right: 0; top: 120px; }
  .card-back .tab-bottom { left: 0; bottom: 40px; }
  .back-brand {
    position: absolute; left: 0; right: 0; top: 140px;
    display: flex; align-items: center; justify-content: center; gap: 14px;
  }
  .brand-square { width: 26px; height: 26px; }
  .back-brand .brand-square { background: var(--silver); }
  .back-brand .brand-name {
    color: var(--silver); font-weight: 700; font-size: 34px;
    letter-spacing: 2px; text-transform: uppercase;
  }
  .tagline {
    position: absolute; left: 0; right: 0; top: 262px; text-align: center;
    font-family: "Oswald", sans-serif; font-weight: 300;
    color: var(--green); font-size: 16px; letter-spacing: 2px; text-transform: uppercase;
  }

  /* Front of card */
  .card-front { left: 380px; top: 472px; background: var(--paper); }
  .front-brand {
    position: absolute; right: 48px; top: 40px;
    display: flex; align-items: center; gap: 10px;
  }
  .front-brand .brand-square { background: var(--navy); width: 22px; height: 22px; }
  .front-brand .brand-name {
    color: var(--navy); font-weight: 700; font-size: 26px;
    letter-spacing: 1.5px; text-transform: uppercase;
  }
  .rule {
    position: absolute; left: 60px; right: 48px; top: 110px;
    height: 2px; background: var(--rule);
  }
  .edge-mark {
    position: absolute; left: 0; top: 248px; width: 6px; height: 30px; background: var(--navy);
  }
  .person { position: absolute; left: 40px; top: 228px; }
  .person-name {
    color: var(--green); font-size: 21px; font-weight: 500; text-transform: uppercase;
    letter-spacing: .3px;
  }
  .person-title { color: var(--muted); font-size: 15px; margin-left: 18px; margin-top: 2px; }

  .contacts {
    position: absolute; left: 40px; top: 296px; list-style: none;
  }
  .contacts li {
    display: flex; align-items: center; gap: 12px;
    color: var(--navy-text); font-size: 14.5px; line-height: 25px;
  }
  .contacts svg { width: 14px; height: 14px; flex: none; }

  .address {
    position: absolute; right: 48px; top: 236px; text-align: right;
    color: var(--navy-text); font-size: 14.5px; line-height: 21px;
    font-style: normal;
  }
</style>
</head>
<body>
<main class="canvas">

  <section class="card card-back" aria-label="Card back">
    <span class="tab tab-top"></span>
    <span class="tab tab-bottom"></span>
    <div class="back-brand">
      <span class="brand-square"></span>
      <span class="brand-name">Hollis Ironworks</span>
    </div>
    <p class="tagline">Custom quality fabrications</p>
  </section>

  <section class="card card-front" aria-label="Card front">
    <div class="front-brand">
      <span class="brand-square"></span>
      <span class="brand-name">Hollis Ironworks</span>
    </div>
    <div class="rule"></div>
    <span class="edge-mark"></span>

    <div class="person">
      <p class="person-name">Marisa Kettering</p>
      <p class="person-title">Founder</p>
    </div>

    <ul class="contacts">
      <li>
        <svg viewBox="0 0 24 24" fill="var(--green)"><path d="M6.6 10.8a15.1 15.1 0 0 0 6.6 6.6l2.2-2.2a1 1 0 0 1 1-.25 11.4 11.4 0 0 0 3.6.57 1 1 0 0 1 1 1V20a1 1 0 0 1-1 1A17 17 0 0 1 3 4a1 1 0 0 1 1-1h3.5a1 1 0 0 1 1 1c0 1.25.2 2.45.57 3.57a1 1 0 0 1-.25 1z"/></svg>
        0491 538 274 &amp; (02) 7342 9185
      </li>
      <li>
        <svg viewBox="0 0 24 24" fill="none" stroke="var(--green)" stroke-width="2.4"><rect x="3" y="5" width="18" height="14" rx="1"/><path d="M3 6l9 7 9-7"/></svg>
        info@hollisiw.com.au
      </li>
      <li>
        <svg viewBox="0 0 24 24" fill="none" stroke="var(--green)" stroke-width="2.2"><circle cx="12" cy="12" r="9"/><path d="M3 12h18M12 3c3 3 3 15 0 18M12 3c-3 3-3 15 0 18"/></svg>
        www.hollisiw.com.au
      </li>
    </ul>

    <address class="address">
      Level 22, Carrow House<br>
      Banks Road, NSW 2795
    </address>
  </section>

</main>
</body>
</html>
```